QDV Construction and Remodeling

Prefer a matte black card with some colors that pop, but subtle. Contact info. Show General Contractor professional way. Can you please remove renovations repairs maintenance off of my logo.

Target Market(s)

Property and business investors. Homeowners

Industry/Entity Type

Construction

Contact Information for Business Card

Name: Dorian Falkner, Title: CEO, Phone: 555-216-0394, Email: Dorian@QDVbuildTrx.com, website: www QDVbuildTrx.com

Font styles to use
Other font styles liked:
• Designer choose

Colors

Designer to choose colors to be used in the design.

Requirements
Must have
• Uniqueness. Double sided since it wont let me choose that. Professional look, be eye catching and catchy. QR code to my website
Nice to have
• Matte black background, subtle bright colors that pop, but I am open to anything. I also like black and gold with some red. Possible Harborton Ironclad logo colored stars somewhere around the logo or on the back. Just to rep my city
Should not have
• pink. Something you would see somewhere else. gif pictures or generated pictures.

```html
<!DOCTYPE html>
<html lang="en">
<head>
<meta charset="utf-8">
<title>QDV Construction and Remodeling — Business Card</title>
<link rel="stylesheet" href="https://fonts.googleapis.com/css2?family=Montserrat:wght@400;500;700;800&display=swap">
<style>
  :root {
    --backdrop: #3a3330;
    --card-black: #1c1c1d;
    --card-black-light: #2c2c2d;
    --accent-red: #e8202f;
    --edge-red: #b3121f;
    --text-white: #f4f4f4;
    --text-muted: #d9d9d9;
  }
  * { box-sizing: border-box; margin: 0; padding: 0; }
  html, body {
    width: 1200px;
    height: 716px;
    overflow: hidden;
    background: var(--backdrop);
    font-family: "Montserrat", sans-serif;
  }
  .canvas {
    position: relative;
    width: 1200px;
    height: 716px;
  }
  .card {
    position: absolute;
    top: 205px;
    width: 525px;
    height: 300px;
    border-radius: 6px;
    background: linear-gradient(135deg, var(--card-black-light) 0%, var(--card-black) 55%);
    overflow: hidden;
  }
  .card--front {
    left: 45px;
    box-shadow: 0 2px 0 var(--edge-red), 0 4px 0 #8e0e18, 0 6px 0 var(--edge-red), 0 8px 0 #8e0e18, 0 10px 0 var(--edge-red), 0 22px 30px rgba(0,0,0,0.5);
  }
  .card--back {
    left: 630px;
    box-shadow: 0 3px 0 var(--edge-red), 0 18px 30px rgba(0,0,0,0.45);
  }

  .brand {
    display: flex;
    align-items: center;
    gap: 10px;
    color: var(--text-white);
    font-weight: 700;
    text-transform: uppercase;
    line-height: 1.2;
  }
  .brand__mark {
    flex: none;
    background: var(--accent-red);
  }
  .card--front .brand {
    position: absolute;
    left: 30px;
    top: 120px;
    width: 200px;
    font-size: 13px;
    letter-spacing: 0.4px;
  }
  .card--front .brand__mark { width: 12px; height: 12px; }

  .divider {
    position: absolute;
    left: 244px;
    top: 80px;
    width: 2px;
    height: 140px;
    background: var(--accent-red);
  }

  .contact {
    position: absolute;
    left: 266px;
    top: 84px;
    width: 245px;
  }
  .contact__name {
    color: var(--accent-red);
    font-weight: 800;
    font-size: 21px;
    text-transform: uppercase;
    letter-spacing: 0.2px;
    line-height: 1.1;
    white-space: nowrap;
  }
  .contact__title {
    color: var(--text-muted);
    font-size: 12px;
    font-weight: 500;
    margin-top: 3px;
    margin-bottom: 18px;
  }
  .contact__list { list-style: none; }
  .contact__item {
    display: flex;
    align-items: center;
    gap: 7px;
    color: var(--text-white);
    font-size: 12px;
    font-weight: 400;
    margin-bottom: 7px;
    white-space: nowrap;
  }
  .contact__icon {
    width: 10px;
    height: 10px;
    flex: none;
  }
  .contact__highlight { color: var(--accent-red); }

  .card--back .brand {
    position: absolute;
    inset: 0;
    justify-content: center;
    font-size: 28px;
    letter-spacing: 1px;
    gap: 16px;
  }
  .card--back .brand__mark { width: 22px; height: 22px; }
</style>
</head>
<body>
<main class="canvas">

  <section class="card card--front" aria-label="Business card front">
    <div class="brand">
      <span class="brand__mark" aria-hidden="true"></span>
      <span class="brand__name">QDV Construction and Remodeling</span>
    </div>

    <div class="divider" aria-hidden="true"></div>

    <div class="contact">
      <h1 class="contact__name">Dorian Falkner</h1>
      <p class="contact__title">CEO</p>
      <ul class="contact__list">
        <li class="contact__item">
          <svg class="contact__icon" viewBox="0 0 24 24" aria-hidden="true"><path fill="#e8202f" d="M6.6 10.8a15.1 15.1 0 0 0 6.6 6.6l2.2-2.2a1 1 0 0 1 1-.25 11.4 11.4 0 0 0 3.6.57 1 1 0 0 1 1 1V20a1 1 0 0 1-1 1A17 17 0 0 1 3 4a1 1 0 0 1 1-1h3.5a1 1 0 0 1 1 1c0 1.25.2 2.45.57 3.57a1 1 0 0 1-.25 1z"/></svg>
          555-216-0394
        </li>
        <li class="contact__item">
          <svg class="contact__icon" viewBox="0 0 24 24" aria-hidden="true"><rect x="2" y="5" width="20" height="14" rx="1" fill="none" stroke="#e8202f" stroke-width="2.2"/><path d="M2 6l10 7 10-7" fill="none" stroke="#e8202f" stroke-width="2.2"/></svg>
          Dorian@QDVbuildTrx.com
        </li>
        <li class="contact__item">
          <svg class="contact__icon" viewBox="0 0 24 24" aria-hidden="true"><circle cx="12" cy="12" r="9.5" fill="none" stroke="#e8202f" stroke-width="2.2"/><path d="M2.5 12h19M12 2.5c3 3 3 16 0 19M12 2.5c-3 3-3 16 0 19" fill="none" stroke="#e8202f" stroke-width="1.8"/></svg>
          <span>www.<span class="contact__highlight">QDVBUILDTRX</span>.com</span>
        </li>
      </ul>
    </div>
  </section>

  <section class="card card--back" aria-label="Business card back">
    <div class="brand">
      <span class="brand__mark" aria-hidden="true"></span>
      <span class="brand__name">QDV Construction<br>and Remodeling</span>
    </div>
  </section>

</main>
</body>
</html>
```